Zo Fen smart screen Flyer design

Hi,

Please see attached file as I have done up a very very basic flyer just with the information that will need to be presented.

Please don't go with this as a format I would like, as I have no design skills at all.

I'm looking for something that is basic but professional looking capturing this information.
I would prefer if the symbols were changed so they were all consistent and the colour scheme worked together with the logo.

If you can use the picture of the screen provided as I will replace this once my product has its photoshoot.

Thanks!

```html
<!DOCTYPE html>
<html lang="en">
<head>
<meta charset="utf-8">
<title>Zo Fen Smart Screen Flyer</title>
<link href="https://fonts.googleapis.com/css2?family=Mulish:wght@400;600;700;800&display=swap" rel="stylesheet">
<style>
  :root{
    --ink:#141414;
    --text:#2b2b2b;
    --stage:#d9d9d9;
    --paper:#ffffff;
    --mist:#e4e4e6;
    --magenta:#c04a9e;
    --cyan:#49c3ec;
    --yellow:#fbd90c;
    --rule:#cfcfcf;
  }
  *{box-sizing:border-box;margin:0;padding:0}
  html,body{width:1200px;height:1200px;overflow:hidden}
  body{background:var(--stage);font-family:'Mulish',sans-serif;color:var(--text);position:relative}
  .flyer{position:absolute;left:150px;top:21px;width:900px;height:1158px;
    background:linear-gradient(180deg,#f7f7f8 0,var(--mist) 300px,#eeeef0 480px,var(--paper) 590px,var(--paper) 100%);overflow:hidden}
  .brand{position:absolute;left:68px;top:100px;display:flex;align-items:center;gap:14px}
  .brand-square{width:22px;height:22px;background:var(--magenta)}
  .brand-name{font-size:44px;font-weight:800;color:var(--ink);letter-spacing:1px}
  .headline{position:absolute;left:61px;top:218px;font-size:28px;font-weight:700;line-height:42px;color:var(--ink)}
  .accent{display:inline-block;position:relative;width:116px;height:14px;margin-left:10px;vertical-align:middle}
  .accent i{position:absolute;height:3px}
  .accent .y{left:0;top:0;width:70px;background:var(--yellow)}
  .accent .c{left:84px;top:0;width:32px;background:var(--cyan)}
  .accent .m{left:47px;top:10px;width:47px;background:var(--magenta)}
  .intro{position:absolute;left:61px;top:378px;width:335px;font-size:15.5px;line-height:24px}
  .intro p+p{margin-top:24px}
  .deco-pink{position:absolute;left:422px;top:124px;width:99px;height:99px;background:linear-gradient(135deg,#f3dcea,#cf82b5)}
  .deco-yellow{position:absolute;left:496px;top:104px;width:39px;height:39px;background:linear-gradient(135deg,#fff6b0,#fde66a)}
  .product-photo{position:absolute;left:464px;top:140px;width:371px;height:440px;
    background:linear-gradient(135deg,#7fc4b4 0%,#b98ab8 50%,#f3b66a 100%)}
  .feature{position:absolute;display:flex;gap:18px}
  .icon-tile{width:119px;height:109px;flex:none;display:flex;align-items:center;justify-content:center}
  .icon-tile svg{width:78px;height:78px;fill:none;stroke:#fff;stroke-width:3.2;stroke-linecap:round}
  .tile-4g{background:linear-gradient(180deg,#f3dcec,#c44c9d)}
  .tile-temp{background:linear-gradient(180deg,#f9ad92,#ee4526)}
  .tile-wifi{background:linear-gradient(180deg,#e6f6fd,#49c3ec)}
  .tile-award{background:linear-gradient(180deg,#e6f3dd,#6cbf45)}
  .tile-sun{background:linear-gradient(180deg,#fff7d8,#fbd90c)}
  .feature-text{padding-top:6px}
  .feature-title{font-size:20px;font-weight:700;color:var(--ink);line-height:24px;margin-bottom:4px}
  .feature-body{font-size:15.5px;line-height:24px}
  .f1{left:55px;top:606px}.f2{left:448px;top:606px}
  .f3{left:55px;top:747px}.f4{left:448px;top:747px}
  .f5{left:55px;top:889px}
  .f1 .feature-body{width:190px}
  .f3 .feature-body{width:212px}
  .f2 .feature-body,.f4 .feature-body{width:265px}
  .f5 .feature-body{width:400px}
  .rule{position:absolute;left:55px;top:1036px;width:791px;height:2px;background:var(--rule)}
  .cta{position:absolute;left:55px;top:1073px;font-size:17px;font-weight:700;line-height:22px;color:var(--ink)}
  .phone-badge{position:absolute;left:217px;top:1074px;width:47px;height:47px;border-radius:50%;
    background:linear-gradient(180deg,#a7e2f7,#49c3ec);display:flex;align-items:center;justify-content:center}
  .phone-number{position:absolute;left:275px;top:1074px;font-size:34px;font-weight:400;color:var(--ink);line-height:46px}
  .contact{position:absolute;right:54px;top:1062px;font-size:16.5px;line-height:33px;color:var(--ink);text-align:right}
  .contact div{display:flex;align-items:center;justify-content:flex-end;gap:7px}
  .contact svg{width:14px;height:14px}
</style>
</head>
<body>
<main class="flyer">
  <div class="brand"><span class="brand-square"></span><span class="brand-name">Zo Fen</span></div>

  <h1 class="headline">Bring Attention to Your<br>Bussiness with Your Own<br>HD LED Display<span class="accent"><i class="y"></i><i class="c"></i><i class="m"></i></span></h1>

  <div class="intro">
    <p>Our displays can be mounted outdoors on walls, roofs, fixed signs, trailer mounted ect.</p>
    <p>We also do indoor led screens for shop fronts and display stands. All screens are custom built to your requirements including size, shape and even curved displays</p>
  </div>

  <div class="deco-pink"></div>
  <div class="deco-yellow"></div>
  <div class="product-photo" role="img" aria-label="Product photo of an LED display screen"></div>

  <section class="feature f1">
    <div class="icon-tile tile-4g"><svg viewBox="0 0 80 80"><path d="M18 28a32 32 0 0 1 44 0M25 35a22 22 0 0 1 30 0M32 42a12 12 0 0 1 16 0"/><text x="40" y="72" text-anchor="middle" fill="#fff" stroke="none" font-family="Mulish,sans-serif" font-size="26" font-weight="700">4G</text></svg></div>
    <div class="feature-text"><h2 class="feature-title">4G CAPABLE</h2><p class="feature-body">Change screen content with a click of the mouse anywhere in the world</p></div>
  </section>

  <section class="feature f2">
    <div class="icon-tile tile-temp"><svg viewBox="0 0 80 80"><path d="M35 50V16a5 5 0 0 1 10 0v34a10 10 0 1 1-10 0z"/><circle cx="40" cy="58" r="4"/><line x1="40" y1="54" x2="40" y2="30"/><path d="M20 22v10M15 27h10M16.5 23.5l7 7M23.5 23.5l-7 7" stroke-width="2"/><circle cx="60" cy="27" r="3.5" stroke-width="2"/><path d="M60 19v3M60 32v3M52 27h3M65 27h3" stroke-width="2"/></svg></div>
    <div class="feature-text"><h2 class="feature-title">ONLINE MONITORING</h2><p class="feature-body">Monitor cabinet temperature and humidity plus more in real time online. Recieve alerts via email.</p></div>
  </section>

  <section class="feature f3">
    <div class="icon-tile tile-wifi"><svg viewBox="0 0 80 80"><path d="M8 32a46 46 0 0 1 64 0M17 41a33 33 0 0 1 46 0M26 50a20 20 0 0 1 28 0"/><circle cx="40" cy="62" r="3" fill="#fff"/></svg></div>
    <div class="feature-text"><h2 class="feature-title">WIFI CAPABLE</h2><p class="feature-body">Change screen content with a PC, tablet or mobile phone with an easy to use app</p></div>
  </section>

  <section class="feature f4">
    <div class="icon-tile tile-award"><svg viewBox="0 0 80 80"><circle cx="40" cy="32" r="20"/><circle cx="40" cy="32" r="13"/><path d="M40 24l2.4 5 5.4.6-4 3.7 1.1 5.3L40 36l-4.9 2.6 1.1-5.3-4-3.7 5.4-.6z" stroke-width="2"/><path d="M32 51v18l8-6 8 6V51"/></svg></div>
    <div class="feature-text"><h2 class="feature-title">HIGH QUALITY PRODUCTS</h2><p class="feature-body">Change screen content with a PC, tablet or mobile phone with an easy to use app</p></div>
  </section>

  <section class="feature f5">
    <div class="icon-tile tile-sun"><svg viewBox="0 0 80 80"><circle cx="40" cy="40" r="14"/><path d="M40 26v28a14 14 0 0 0 0-28z" fill="#fff"/><path d="M40 10v7M40 63v7M10 40h7M63 40h7M19 19l5 5M56 56l5 5M61 19l-5 5M24 56l-5 5"/></svg></div>
    <div class="feature-text"><h2 class="feature-title">INTELLIGENT BRIGHTNESS CONTROL</h2><p class="feature-body">Screen will automatically adjust to suit ambiant light improving screen veiwing quality and saving in power consumption</p></div>
  </section>

  <div class="rule"></div>

  <p class="cta">CALL US NOW<br>FOR FREE QUOTE</p>
  <div class="phone-badge"><svg viewBox="0 0 24 24" width="24" height="24"><path d="M6.6 10.8a15 15 0 0 0 6.6 6.6l2.2-2.2c.3-.3.7-.4 1-.2 1.1.4 2.3.6 3.6.6.6 0 1 .4 1 1V20c0 .6-.4 1-1 1A17 17 0 0 1 3 4c0-.6.4-1 1-1h3.5c.6 0 1 .4 1 1 0 1.300.2 2.500.6 3.6.1.3 0 .7-.2 1z" fill="#fff"/></svg></div>
  <p class="phone-number">1300 960 418</p>

  <div class="contact">
    <div><svg viewBox="0 0 24 24" fill="none" stroke="#141414" stroke-width="2"><circle cx="12" cy="12" r="10"/><path d="M2 12h20M12 2a15 15 0 0 1 0 20M12 2a15 15 0 0 0 0 20"/></svg>www.zofenscreens.com.au</div>
    <div><svg viewBox="0 0 24 24"><path d="M2 5h20v14H2z" fill="#141414"/><path d="M2 6l10 7 10-7" fill="none" stroke="#fff" stroke-width="2"/></svg>hello@zofenscreens.com.au</div>
  </div>
</main>
</body>
</html>
```